2 page flyer outlining details of a product framework

We need a flyer for a management consulting firm outlining a product we offer. The draft wording and company logo are attached. Logo colours should be used (Purple - C73, M93, Y0, K0 & Green - C50, M0, Y99, K0).
The look and feel should communicate a dynamic, trustworthy, credible organisation with excellence in delivery.

File must be provided in AI format to enable text changes.

Target Market(s)

Senior Business Excecutives

Industry/Entity Type

Management Consulting

Font styles to use
Other font styles liked:
• Aller & Myriad Pro

Colors
acd036
6b449b

Requirements
Must have
• Logo & wording provided, professional images and a flyer layout with space and a section for contact details.

```html
<!DOCTYPE html>
<html lang="en">
<head>
<meta charset="utf-8">
<title>Meridian Management Consulting – Flyer</title>
<link href="https://fonts.googleapis.com/css2?family=Source+Sans+3:wght@300;400;600;700&display=swap" rel="stylesheet">
<style>
  :root {
    --brand-purple: #673894;
    --brand-green: #8dc63f;
    --paper-white: #ffffff;
    --accent-tint: rgba(255, 255, 255, 0.13);
    --canvas-bg: #ffffff;
  }
  * { margin: 0; padding: 0; box-sizing: border-box; }
  html, body {
    width: 1200px;
    height: 1000px;
    overflow: hidden;
    background: var(--canvas-bg);
    font-family: "Source Sans 3", "Myriad Pro", sans-serif;
  }
  .flyer-page {
    position: absolute;
    left: 247px;
    top: 27px;
    width: 665px;
    height: 940px;
    background: var(--brand-purple);
    color: var(--paper-white);
    overflow: hidden;
  }
  .accent-disc {
    position: absolute;
    left: 200px;
    top: 395px;
    width: 560px;
    height: 560px;
    border-radius: 50%;
    background: var(--accent-tint);
  }
  .brand-lockup {
    position: absolute;
    left: 82px;
    top: 104px;
    display: flex;
    align-items: center;
  }
  .brand-mark {
    width: 172px;
    height: 172px;
    border-radius: 50%;
    background: var(--brand-green);
    flex: none;
    margin-right: 24px;
  }
  .brand-name {
    font-weight: 600;
    color: var(--paper-white);
    line-height: 1;
  }
  .brand-name__primary {
    display: block;
    font-size: 66px;
    letter-spacing: 0.5px;
  }
  .brand-name__secondary {
    display: block;
    font-size: 24px;
    letter-spacing: 1.4px;
    margin-top: 2px;
  }
  .pitch {
    position: absolute;
    left: 82px;
    top: 395px;
    width: 260px;
    white-space: nowrap;
  }
  .pitch__question {
    font-size: 21px;
    font-weight: 300;
    line-height: 27px;
    margin-bottom: 11px;
    letter-spacing: -0.2px;
  }
  .pitch__question strong { font-weight: 600; }
  .pitch__offer {
    font-size: 21px;
    font-weight: 300;
    line-height: 27px;
    color: var(--brand-green);
    letter-spacing: -0.2px;
  }
  .pitch__offer strong { font-weight: 700; }
  .pitch__body {
    margin-top: 20px;
    font-size: 14px;
    font-weight: 400;
    line-height: 19px;
    letter-spacing: -0.2px;
  }
  .pitch__body strong { font-weight: 700; }
</style>
</head>
<body>
  <main class="flyer-page">
    <span class="accent-disc" aria-hidden="true"></span>

    <header class="brand-lockup">
      <span class="brand-mark" aria-hidden="true"></span>
      <h1 class="brand-name">
        <span class="brand-name__primary">MERIDIAN</span>
        <span class="brand-name__secondary">Management Consulting</span>
      </h1>
    </header>

    <section class="pitch">
      <p class="pitch__question">How <strong>much</strong> is inefficient<br>workforce management<br><strong>costing</strong> your business?</p>
      <p class="pitch__question">Are you as <strong>efficient</strong> as<br>you could be?</p>
      <p class="pitch__offer">Find the answers with a<br>powerful <strong>Fully Optimised<br>Workforce ™ (FOW!)<br>Framework Assessment!</strong></p>
      <p class="pitch__body">We provide a detailed, tailored<br>assessment based on our proprietary<br><strong>FOW! Framework</strong>.&nbsp; Our framework<br>is scalable and flexible to suit<br>organisations of any size and<br>structure – providing you with a<br>roadmap to successfully achieving<br>better business outcomes, greater<br>efficiency, and cost savings.</p>
    </section>
  </main>
</body>
</html>
```